Business price tag design for Furniture Business

Hello,

I have developed a tag for a home furniture business and need 1 more creative template. Please see attachment. I need the template to be very appealing.

Requirements:

1.Tag dimensions needs to be about the same as attached tag.
2. Tag design needs to be suitable for a home furniture business.
3. Tag needs to have locations for the following: Item Title, Now Price, Was Price, Product Number.
4. "The black shape at the bottom of attached tag could be removed.

I have no requirements on colors, but something professional is needed, preferably white background to reduce print ink consumption.

Please see attachment for clarification.

Industry/Entity Type

Retail

Font styles to use
Serif
Sans Serif

Requirements
Must have
• Please see Project Description.
Nice to have

```html
<!DOCTYPE html>
<html lang="en">
<head>
<meta charset="utf-8">
<title>Summit Furniture Outlet – Price Tag</title>
<link href="https://fonts.googleapis.com/css2?family=Roboto+Condensed:wght@400;700&display=swap" rel="stylesheet">
<style>
  :root {
    --coral: #e8674a;
    --coral-deep: #e4553a;
    --cream: #f7f1e4;
    --cream-ray: #efe4cf;
    --brown: #6b3a28;
    --white: #ffffff;
  }
  * { margin: 0; padding: 0; box-sizing: border-box; }
  html, body { width: 1200px; height: 2416px; overflow: hidden; }
  body { background: var(--coral); font-family: "Roboto Condensed", "Arial Narrow", sans-serif; }
  .tag { position: relative; width: 1200px; height: 2416px; background: var(--coral); overflow: hidden; }

  .showroom-photo {
    position: absolute; left: 40px; top: 32px; width: 1120px; height: 928px;
    background:
      linear-gradient(180deg, #e9e9e8 0%, #dcdcdb 45%, #bdbab4 62%, #4a3f38 78%, #2e2722 100%);
  }
  .corner-curve { position: absolute; }
  .corner-curve--top-left { left: 0; top: 0; }
  .corner-curve--top-right { right: 0; top: 0; }
  .corner-curve--bottom-right { right: 0; bottom: 0; }

  .store-band {
    position: absolute; left: 0; top: 990px; width: 1200px; height: 170px;
    display: flex; align-items: center; padding-left: 112px; gap: 28px;
    color: var(--white); text-transform: uppercase;
  }
  .store-name__main { font-weight: 700; font-size: 124px; letter-spacing: 1px; }
  .store-name__sub { font-weight: 400; font-size: 70px; letter-spacing: 1px; padding-top: 20px; }

  .price-panel {
    position: absolute; left: 40px; top: 1196px; width: 1120px; height: 1180px;
    background: radial-gradient(circle at 85% 45%, var(--cream) 0%, var(--cream) 30%, var(--cream-ray) 100%);
  }
  .price-panel__text { position: absolute; left: 84px; color: var(--brown); line-height: 1; }
  .item-title { top: 130px; font-size: 100px; font-weight: 700; }
  .product-number { top: 268px; font-size: 100px; font-weight: 700; }
  .was-label { top: 410px; font-size: 108px; font-weight: 400; }
  .was-price { top: 560px; font-size: 108px; font-weight: 700; }
  .now-label { top: 750px; font-size: 116px; font-weight: 700; }
  .you-save { top: 1000px; font-size: 76px; font-weight: 700; }

  .now-price {
    position: absolute; left: 672px; top: 712px; width: 448px; height: 192px;
    background: var(--coral-deep); color: var(--white);
    font-size: 148px; font-weight: 700; line-height: 192px; padding-left: 40px;
  }
</style>
</head>
<body>
<div class="tag">
  <div class="showroom-photo" role="img" aria-label="Photo of a bright modern living room with a beige sofa, rug, white chair and wall shelves"></div>

  <svg class="corner-curve corner-curve--top-left" width="260" height="200" viewBox="0 0 260 200">
    <path d="M0 0 H260 C150 10 60 60 0 200 Z" fill="var(--coral)"/>
  </svg>
  <svg class="corner-curve corner-curve--top-right" width="180" height="130" viewBox="0 0 180 130">
    <path d="M180 0 H0 C90 10 150 50 180 130 Z" fill="var(--coral)"/>
  </svg>

  <header class="store-band">
    <span class="store-name__main">Summit</span>
    <span class="store-name__sub">Furniture Outlet</span>
  </header>

  <section class="price-panel">
    <p class="price-panel__text item-title">Black Queen Bed</p>
    <p class="price-panel__text product-number">B4350</p>
    <p class="price-panel__text was-label">COMPARE</p>
    <p class="price-panel__text was-price">AT:&nbsp; $ 500</p>
    <p class="price-panel__text now-label">Only for</p>
    <div class="now-price">$ 450</div>
    <p class="price-panel__text you-save">You Save: $50</p>
  </section>

  <svg class="corner-curve corner-curve--bottom-right" width="260" height="220" viewBox="0 0 260 220">
    <path d="M260 220 V0 C200 30 120 120 0 220 Z" fill="var(--coral)"/>
  </svg>
</div>
</body>
</html>
```